Have Logo - Need Business Card Design!!!

I am looking for a business card design for a real estate development business. The company name is Halvern Crest Properties. I already have a logo created by Artisan Hive and would like this logo to be incorporated into the design. I have uploaded the files. The card needs to be professional, but visually interesting. Not necessary to be double-sided, but if you want to get creative and can think of something to put on the back then have at it.

Target Market(s)

The target audience for these business cards will be professionals in the real estate industry.

Industry/Entity Type

Real Estate

Requirements
Must have
• The business card must have all the necessary items for a business card, i.e. company name, our logo, name (however, not title necessary), office address, office phone number, cell number, fax number, website address, etc.

You can use the information below for the card:

Gregory L. Danforth
718 Ridgemont Avenue
San Francisco, California 94382

www.halverncrest.example
gdanforth@halverncrest.example
Office: 415-555-0143
Fax: 415-555-0147
Cell: 415-555-0186

```html
<!DOCTYPE html>
<html lang="en">
<head>
<meta charset="utf-8">
<title>Halvern Crest Properties – Business Card</title>
<link rel="stylesheet" href="https://fonts.googleapis.com/css2?family=Open+Sans:wght@400;600&display=swap">
<style>
  :root {
    --navy: #34306f;
    --paper: #f1f1ef;
    --green: #2f8a3f;
    --name-green: #3a9a4a;
    --backdrop: #e4e4e6;
    --ink-light: #ffffff;
    --ink-dark: #2a2760;
  }
  * { box-sizing: border-box; margin: 0; padding: 0; }
  html, body { width: 1200px; height: 800px; overflow: hidden; }
  body {
    background: var(--backdrop);
    font-family: "Open Sans", Arial, sans-serif;
    position: relative;
  }
  .card {
    position: absolute;
    top: 245px;
    width: 540px;
    height: 310px;
    background: var(--navy);
    overflow: hidden;
  }
  .card--front { left: 40px; }
  .card--back { left: 620px; }

  .wordmark {
    position: absolute;
    display: flex;
    align-items: center;
    color: var(--green);
    font-weight: 600;
    white-space: nowrap;
  }
  .wordmark__square { background: var(--green); flex: none; }

  /* Front */
  .front__logo-band {
    position: absolute;
    left: 12px; top: 12px;
    width: 452px; height: 108px;
    background: var(--paper);
  }
  .front__logo-band .wordmark {
    left: 70px; top: 50%;
    transform: translateY(-50%);
    font-size: 22px;
    gap: 10px;
  }
  .front__logo-band .wordmark__square { width: 24px; height: 24px; }

  .holder-name {
    position: absolute;
    left: 30px; top: 128px;
    color: var(--name-green);
    font-size: 17px;
    font-weight: 400;
    line-height: 22px;
  }
  .contact-list {
    position: absolute;
    list-style: none;
    color: var(--ink-light);
    font-size: 12.5px;
    line-height: 18px;
  }
  .contact-list--phones { left: 30px; top: 154px; }
  .contact-list--online { left: 238px; top: 154px; }

  .front__address-band {
    position: absolute;
    left: 150px; top: 214px;
    width: 378px; height: 84px;
    background: var(--paper);
  }
  .address {
    position: absolute;
    left: 20px; top: 15px;
    font-style: normal;
    color: var(--ink-dark);
    font-size: 12.5px;
    line-height: 18px;
  }

  /* Back */
  .back__panel {
    position: absolute;
    left: 14px; top: 14px;
    width: 512px; height: 282px;
    background: var(--paper);
  }
  .back__notch {
    position: absolute;
    top: 100px;
    width: 26px; height: 110px;
    background: var(--navy);
  }
  .back__notch--left { left: 0; }
  .back__notch--right { right: 0; }
  .card--back .wordmark {
    left: 50%; top: 50%;
    transform: translate(-50%, -50%);
    font-size: 31px;
    gap: 12px;
  }
  .card--back .wordmark__square { width: 34px; height: 34px; }
</style>
</head>
<body>
  <section class="card card--front" aria-label="Business card front">
    <div class="front__logo-band">
      <div class="wordmark"><span class="wordmark__square"></span>Halvern Crest Properties</div>
    </div>
    <h1 class="holder-name">Gregory L. Danforth</h1>
    <ul class="contact-list contact-list--phones">
      <li>Tel: 415-555-0186</li>
      <li>Fax: 415-555-0147</li>
      <li>Office: 415-555-0143</li>
    </ul>
    <ul class="contact-list contact-list--online">
      <li>Web: www.halverncrest.example</li>
      <li>Email: gdanforth@halverncrest.example</li>
    </ul>
    <div class="front__address-band">
      <address class="address">
        Halvern Crest Properties<br>
        718 Ridgemont Avenue<br>
        San Francisco, California 94382
      </address>
    </div>
  </section>

  <section class="card card--back" aria-label="Business card back">
    <div class="back__panel">
      <span class="back__notch back__notch--left"></span>
      <span class="back__notch back__notch--right"></span>
      <div class="wordmark"><span class="wordmark__square"></span>Halvern Crest Properties</div>
    </div>
  </section>
</body>
</html>
```